Flyer Design

Meadowbright Cleaning Service LTD its all about cleaning ( Domestic Cleaning, Commercial Cleaning, Student Accommodations, Corridors, Halls & Common Areas). I'm looking for POSH/ ELEGANT LOOKING design of flyers, which presents all Services we provide, it also should include 5% discount for new customers, contact details: website: www.meadowbright-clean.co.uk email address: meadowbrightservice@mailnest.co.uk Mobile phone no: 07812036471 and home no: 01632960418 . I would like to include logo of the company, without any pictures of buckets etc.(that in my opinion pictures like that looks "cheap"). It should be design which perfectly match logo of the company, I would like also to include slogan of Meadowbright "You Deserve Meadowbright Cleaners". I was thinking to make those flyers, bright "clean" (maybe background could be beige color, on the other hand I think Navy color looks elegant as well, I'm looking for something posh NOT like some random cleaning company, It should be something UNIQUE). Of course by this flyers Meadowbright Cleaning Service should increase profits. If you will have any draft or any questions please contact me at any time on email: i.wrzesniak@mailnest.co.uk or by phone: 07812036471
Best Regards
Ilona Wrzesniak
Meadowbright Cleaning Service LTD

```html
<!DOCTYPE html>
<html lang="en">
<head>
<meta charset="utf-8">
<title>Meadowbright Cleaning Service LTD – Flyer</title>
<link href="https://fonts.googleapis.com/css2?family=Questrial&family=Montserrat:wght@600;700&family=Pinyon+Script&display=swap" rel="stylesheet">
<style>
  :root {
    --page-bg: #ffffff;
    --cyan-deep: #16e0f2;
    --cyan-mid: #5ee9f7;
    --cyan-light: #c4f1fb;
    --ink: #111111;
    --white: #ffffff;
    --bar-white: rgba(255,255,255,0.95);
    --photo-a: #6b4a36;
    --photo-b: #b58a55;
    --photo-c: #3a2a2a;
  }
  * { margin: 0; padding: 0; box-sizing: border-box; }
  html, body { width: 1200px; height: 848px; overflow: hidden; background: var(--page-bg); }
  .canvas { position: relative; width: 1200px; height: 848px; }

  .sheet {
    position: absolute; top: 62px; width: 510px; height: 716px; overflow: hidden;
    box-shadow: 3px 4px 8px rgba(0,0,0,0.35);
    background: linear-gradient(180deg, var(--cyan-light) 0%, #9fe9f8 28%, var(--cyan-mid) 40%, var(--cyan-deep) 60%, var(--cyan-deep) 100%);
  }
  .sheet--cover { left: 60px; }
  .sheet--offer { left: 614px; }

  /* Cover */
  .cover-name {
    position: absolute; left: 74px; top: 244px;
    font-family: "Questrial", "Century Gothic", sans-serif;
    font-size: 40px; line-height: 38px; color: var(--white); letter-spacing: 0.5px;
    font-weight: 400; text-shadow: 0 0 1px var(--white);
  }
  .cover-slogan {
    position: absolute; left: 76px; top: 368px;
    font-family: "Pinyon Script", cursive; font-size: 19px; color: var(--white);
  }
  .cover-contacts {
    position: absolute; left: 0; right: 0; top: 644px;
    font-family: "Questrial", sans-serif; font-size: 12.5px; color: var(--white);
    display: flex; flex-direction: column; align-items: center; gap: 8px;
  }
  .cover-contacts .row { display: flex; gap: 8px; }
  .contact-item { display: flex; align-items: center; gap: 3px; white-space: nowrap; }
  .badge-outline {
    width: 18px; height: 18px; border: 1px solid var(--white); border-radius: 50%;
    font-size: 10px; display: flex; align-items: center; justify-content: center;
  }

  /* Offer */
  .headline-script {
    position: absolute; left: 0; right: 0; top: 38px; text-align: center;
    font-family: "Pinyon Script", cursive; font-size: 68px; color: var(--ink);
  }
  .headline-name {
    position: absolute; left: 0; right: 0; top: 120px; text-align: center;
    font-family: "Montserrat", sans-serif; font-weight: 700; color: var(--ink);
    font-size: 47px; line-height: 54px; letter-spacing: 0.5px;
  }
  .photo-strip {
    position: absolute; left: 0; top: 246px; width: 510px; height: 102px;
    background: linear-gradient(90deg, var(--photo-a) 0%, var(--photo-b) 30%, var(--photo-c) 55%, #8b3b2a 70%, var(--photo-b) 100%);
  }
  .photo-reflection {
    position: absolute; left: 0; top: 348px; width: 510px; height: 70px;
    background: linear-gradient(180deg, rgba(120,150,150,0.55) 0%, rgba(94,233,247,0) 100%);
  }
  .services { position: absolute; left: 0; top: 446px; list-style: none; }
  .services li {
    width: 262px; height: 27px; margin-bottom: 10px; padding-left: 36px;
    display: flex; align-items: center;
    background: linear-gradient(90deg, var(--bar-white) 0%, var(--bar-white) 65%, rgba(255,255,255,0) 100%);
    font-family: "Montserrat", sans-serif; font-weight: 600; font-size: 11px; color: var(--ink);
  }
  .discount {
    position: absolute; left: 282px; top: 444px; width: 201px; height: 150px;
    background: var(--white); border: 3px dotted #bfe9f0; outline: 3px solid var(--white);
    text-align: center; font-family: "Montserrat", sans-serif; color: var(--ink);
  }
  .discount-value { font-size: 78px; font-weight: 700; line-height: 80px; margin-top: 8px; }
  .discount-label { font-size: 25px; font-weight: 700; line-height: 26px; }
  .discount-note { font-size: 9px; font-weight: 600; margin-top: 6px; }
  .brand-mark {
    position: absolute; left: 18px; top: 658px; width: 214px; text-align: center;
    font-family: "Montserrat", sans-serif; font-weight: 600; font-size: 12px; line-height: 16px; color: var(--ink);
  }
  .offer-contacts {
    position: absolute; left: 250px; top: 626px;
    font-family: "Montserrat", sans-serif; font-weight: 600; font-size: 10.5px; color: var(--ink);
    display: flex; flex-direction: column; gap: 6px;
  }
  .offer-contacts .row { display: flex; gap: 6px; }
  .badge-solid {
    width: 18px; height: 18px; border-radius: 50%; background: var(--ink); color: var(--white);
    font-size: 10px; font-weight: 400; display: flex; align-items: center; justify-content: center;
    flex-shrink: 0;
  }
</style>
</head>
<body>
<div class="canvas">

  <section class="sheet sheet--cover">
    <h1 class="cover-name">MEADOWBRIGHT<br>CLEANING<br>SERVICE LTD</h1>
    <p class="cover-slogan">You deserve Meadowbright Cleaners</p>
    <div class="cover-contacts">
      <div class="row">
        <span class="contact-item"><span class="badge-outline">w</span>www.meadowbright-clean.co.uk</span>
        <span class="contact-item"><span class="badge-outline">e</span>meadowbrightservice@mailnest.co.uk</span>
      </div>
      <div class="row">
        <span class="contact-item"><span class="badge-outline">m</span>07812036471</span>
        <span class="contact-item"><span class="badge-outline">p</span>01632960418</span>
      </div>
    </div>
  </section>

  <section class="sheet sheet--offer">
    <p class="headline-script">You deserve</p>
    <h2 class="headline-name">MEADOWBRIGHT<br>CLEANERS</h2>
    <div class="photo-strip" role="img" aria-label="Row of four photographs of elegant cleaned interiors: hallway, bedroom, lounge and dining room"></div>
    <div class="photo-reflection" role="img" aria-label="Mirrored reflection of the interior photographs"></div>

    <ul class="services">
      <li>Domestic Cleaning,</li>
      <li>Commercial Cleaning,</li>
      <li>Student Accommodations,</li>
      <li>Corridors, Halls &amp; Common Areas</li>
    </ul>

    <div class="discount">
      <div class="discount-value">5%</div>
      <div class="discount-label">DISCOUNT</div>
      <div class="discount-note">For all new customers</div>
    </div>

    <p class="brand-mark">MEADOWBRIGHT CLEANING<br>SERVICE LTD</p>

    <div class="offer-contacts">
      <span class="contact-item"><span class="badge-solid">w</span>www.meadowbright-clean.co.uk</span>
      <span class="contact-item"><span class="badge-solid">e</span>meadowbrightservice@mailnest.co.uk</span>
      <div class="row">
        <span class="contact-item"><span class="badge-solid">m</span>07812036471</span>
        <span class="contact-item"><span class="badge-solid">p</span>01632960418</span>
      </div>
    </div>
  </section>

</div>
</body>
</html>
```